Business Card Design

Personal training studio. My colors are burnt orange and grey. Specializing in group training and total body composition change. Nutritional consultant and contest prep.

Target Market(s)

My audience are people who are looking for total body composition change as well as knowledge on how to effectively receive results in the gym that they are a member of.

Industry/Entity Type

Training

Contact Information for Business Card

Dr. Marla Petrov
Marlajpetrov@mailbox-example.com
3125550147
2817 east Bralen ave.
Brookvale Westmere 60999

Colors
f37122
aaaaaa

Requirements
Must have
• Animphasis on gaining knowledge that will sustain them for a life time. Healthy results and notice me results.
Nice to have
• Card should correlate with the colors of the studio. Orange and grey. With black flooring with orange speckles in it.

```html
<!DOCTYPE html>
<html lang="en">
<head>
<meta charset="utf-8">
<title>Forge Point Fitness – Business Card</title>
<link rel="stylesheet" href="https://fonts.googleapis.com/css2?family=Montserrat:wght@400;600;700&family=Open+Sans:wght@400;600&display=swap">
<style>
  :root {
    --backdrop: #3a3533;
    --card-black: #1f1b1a;
    --burnt-orange: #e87c1e;
    --studio-grey: #9c9c9c;
    --text-white: #ffffff;
    --muted-grey: #8a8a8a;
  }
  * { margin: 0; padding: 0; box-sizing: border-box; }
  html, body {
    width: 1200px; height: 768px; overflow: hidden;
    background: var(--backdrop);
  }
  .canvas {
    position: relative; width: 1200px; height: 768px;
  }
  .card {
    position: absolute; top: 230px;
    width: 540px; height: 309px;
    background: var(--card-black);
    overflow: hidden;
    box-shadow: 0 14px 30px rgba(0,0,0,0.45);
  }
  .card--front { left: 40px; }
  .card--back { left: 620px; }

  .brand {
    position: absolute;
    display: flex; align-items: center; gap: 12px;
  }
  .brand__dot {
    width: 40px; height: 40px; border-radius: 50%;
    background: var(--burnt-orange);
    flex: none;
  }
  .brand__name {
    font-family: "Montserrat", sans-serif;
    font-weight: 600;
    color: var(--studio-grey);
    letter-spacing: 1px;
    line-height: 1.1;
    text-transform: uppercase;
    white-space: nowrap;
  }
  .card--front .brand {
    left: 50%; top: 50%; transform: translate(-50%, -50%);
  }
  .card--front .brand__name { font-size: 24px; }
  .card--back .brand { right: 34px; top: 118px; }
  .card--back .brand__dot { width: 32px; height: 32px; }
  .card--back .brand__name { font-size: 19px; }

  .person {
    position: absolute; left: 40px; top: 48px;
  }
  .person__name {
    font-family: "Montserrat", sans-serif;
    font-weight: 700; font-size: 17px;
    color: var(--burnt-orange);
    letter-spacing: 0.3px;
  }
  .person__role {
    font-family: "Open Sans", sans-serif;
    font-size: 11px; color: var(--muted-grey);
    margin-top: 2px;
  }

  .contact-block {
    position: absolute; left: 0; bottom: 0;
    width: 270px; height: 150px;
    background: var(--burnt-orange);
    padding: 20px 16px 0 30px;
    font-family: "Open Sans", sans-serif;
    font-size: 12px; color: var(--text-white);
    line-height: 1.4;
  }
  .contact-line { display: flex; gap: 7px; align-items: flex-start; }
  .contact-line + .contact-line { margin-top: 2px; }
  .contact-line svg { flex: none; margin-top: 3px; }

  .email-strip {
    position: absolute; left: 270px; right: 0; bottom: 0;
    height: 62px;
    background: var(--studio-grey);
    display: flex; align-items: center; gap: 9px;
    padding-left: 22px;
    font-family: "Open Sans", sans-serif;
    font-size: 12px; color: var(--text-white);
    white-space: nowrap;
  }
</style>
</head>
<body>
<div class="canvas">

  <section class="card card--front" aria-label="Card front">
    <div class="brand">
      <span class="brand__dot"></span>
      <span class="brand__name">Forge Point<br>Fitness</span>
    </div>
  </section>

  <section class="card card--back" aria-label="Card back">
    <div class="person">
      <p class="person__name">Dr. Marla Petrov</p>
      <p class="person__role">Personal trainer</p>
    </div>

    <div class="brand">
      <span class="brand__dot"></span>
      <span class="brand__name">Forge Point<br>Fitness</span>
    </div>

    <div class="contact-block">
      <p class="contact-line">
        <svg width="10" height="10" viewBox="0 0 10 10" aria-hidden="true"><path d="M2 0.5 L3.6 2.8 L2.8 3.8 Q4 6 6.2 7.2 L7.2 6.4 L9.5 8 L8.3 9.5 Q4.5 9.5 2 7 Q0 4.5 0.5 1.7 Z" fill="#fff"/></svg>
        <span>3125550147</span>
      </p>
      <p class="contact-line">
        <svg width="10" height="12" viewBox="0 0 10 12" aria-hidden="true"><path d="M5 0 A4 4 0 0 1 9 4 C9 7 5 12 5 12 C5 12 1 7 1 4 A4 4 0 0 1 5 0 Z" fill="#fff"/><circle cx="5" cy="4" r="1.5" fill="#e87c1e"/></svg>
        <span>2817 east Bralen ave. Brookvale<br>Westmere 60999</span>
      </p>
    </div>

    <div class="email-strip">
      <svg width="13" height="10" viewBox="0 0 13 10" aria-hidden="true"><rect x="0.5" y="0.5" width="12" height="9" fill="none" stroke="#e87c1e" stroke-width="1.2"/><path d="M0.5 0.5 L6.5 5.5 L12.5 0.5" fill="none" stroke="#e87c1e" stroke-width="1.2"/></svg>
      <span>Marlajpetrov@mailbox-example.com</span>
    </div>
  </section>

</div>
</body>
</html>
```